International business needs business cards

Our company, DOR Ventures Inc. is in the business of supplying a range construction products with particular emphasis on CEMENT. We have developed our own brand - BRUNVALE MATERIALS - with which to infiltrate the market. We are launching our brand of cement (BRUNVALE Type IS Cement) into the Caribbean which is unlike anything this market has ever seen. A monopoly has existed here for the past 60-odd years and the market has now opened to allow the importation of other brands and consumers are anxious and ready for change/improvement. We are very excited to be launching and want to make a great first impression. We will be conducting workshops and seminars (from government level to the hardware store owners) and we want our business card to give us the strong, confident introduction that we need.

Target Market(s)

construction; builders; engineers; home owners

Industry/Entity Type

Construction

Contact Information for Business Card

Marisol Penwick
CEO
cell # 1 555 4817730
Ground floor,Lantern Plaza Suite 2483
George Town,Grand Cayman
Cayman Islands,KY1-2250
EMAIL: m.penwick@dorventuresinc.example
web site dorventuresinc.example

COMPANY: skype info dor.ventures.example

second card
Tamsin Rowe-Penwick
CFO
CELL# 1 555 604 3917
George Town,Grand Cayman
Cayman Islands,KY1-2250
EMAIL: t.rowepenwick@dorventuresinc.example
website dorventuresinc.example

Requirements
Must have
• Business cards must display BOTH logos - DOR is the company and BRUNVALE is the brand.

```html
<!DOCTYPE html>
<html lang="en">
<head>
<meta charset="utf-8">
<title>DOR Ventures Inc. – Business Cards</title>
<link rel="stylesheet" href="https://fonts.googleapis.com/css2?family=Open+Sans:wght@400;600;700&display=swap">
<style>
  :root {
    --page-bg: #e9e6e1;
    --card-black: #0c0c0c;
    --card-white: #ffffff;
    --brand-red: #8e1a1c;
    --brand-red-dark: #6f1214;
    --ink: #111111;
    --text-grey: #6b6b6b;
    --url-grey: #cfcfcf;
  }
  * { margin: 0; padding: 0; box-sizing: border-box; }
  html, body { width: 1200px; height: 950px; overflow: hidden; }
  body {
    background: var(--page-bg);
    font-family: "Open Sans", Arial, sans-serif;
    position: relative;
  }
  .card {
    position: absolute;
    width: 700px;
    height: 400px;
    box-shadow: 0 6px 18px rgba(0,0,0,0.25);
    overflow: hidden;
  }

  /* Back of card */
  .card-back {
    left: 60px; top: 50px;
    background: linear-gradient(160deg, #2a2a2a 0%, var(--card-black) 45%, #000 100%);
  }
  .back-mark {
    position: absolute;
    left: 0; right: 0; top: 120px;
    display: flex; align-items: center; justify-content: center; gap: 16px;
  }
  .back-mark .mark-square {
    width: 56px; height: 56px; background: var(--brand-red);
  }
  .back-mark .mark-name {
    color: #ffffff; font-weight: 700; font-size: 34px; letter-spacing: 0.5px;
  }
  .back-url {
    position: absolute; left: 0; right: 0; top: 300px;
    text-align: center; color: var(--url-grey);
    font-size: 17px; letter-spacing: 5px;
  }

  /* Front of card */
  .card-front {
    left: 440px; top: 500px;
    background: var(--card-white);
  }
  .front-top-band {
    position: absolute; left: 0; top: 0; width: 100%; height: 46px;
    background: linear-gradient(180deg, var(--brand-red) 0%, var(--brand-red-dark) 100%);
  }
  .front-name-block {
    position: absolute; left: 0; top: 0; width: 400px; height: 150px;
    background: linear-gradient(180deg, var(--brand-red) 0%, var(--brand-red-dark) 100%);
    padding: 80px 0 0 34px;
    color: #fff;
  }
  .person-name { font-size: 25px; font-weight: 700; }
  .person-title { font-size: 15px; margin-top: 2px; }

  .address {
    position: absolute; left: 34px; top: 178px;
    color: var(--text-grey); font-size: 15px; line-height: 21px;
  }
  .contacts {
    position: absolute; left: 34px; top: 278px;
    list-style: none; color: var(--text-grey); font-size: 15px;
  }
  .contacts li {
    display: flex; align-items: center; gap: 10px; height: 26px;
  }
  .contacts svg { width: 16px; height: 16px; flex: none; fill: var(--brand-red); }

  .brand-mark {
    position: absolute; left: 440px; top: 70px; width: 220px;
    display: flex; align-items: center; gap: 10px;
  }
  .brand-mark .brand-circle {
    width: 58px; height: 58px; border-radius: 50%; background: #6a6a6a;
  }
  .brand-mark .brand-name {
    color: #555555; font-size: 22px; font-weight: 700; letter-spacing: 1px;
  }
  .company-mark {
    position: absolute; left: 400px; top: 230px;
    display: flex; align-items: center; gap: 12px;
  }
  .company-mark .mark-square {
    width: 66px; height: 66px; background: var(--brand-red);
  }
  .company-mark .mark-name {
    color: var(--ink); font-size: 25px; font-weight: 700;
  }
</style>
</head>
<body>

  <section class="card card-back">
    <div class="back-mark">
      <div class="mark-square"></div>
      <div class="mark-name">DOR Ventures Inc.</div>
    </div>
    <p class="back-url">www.dorventuresinc.example</p>
  </section>

  <section class="card card-front">
    <div class="front-top-band"></div>
    <div class="front-name-block">
      <p class="person-name">Marisol Penwick</p>
      <p class="person-title">CEO</p>
    </div>

    <address class="address" style="font-style:normal">
      Ground floor<br>
      Lantern Plaza Suite 2483<br>
      George Town,Grand Cayman<br>
      Cayman Islands,KY1-2250
    </address>

    <ul class="contacts">
      <li>
        <svg viewBox="0 0 16 16" aria-hidden="true"><path d="M4 0h8a1 1 0 0 1 1 1v14a1 1 0 0 1-1 1H4a1 1 0 0 1-1-1V1a1 1 0 0 1 1-1zm1 2v10h6V2zm3 11a1 1 0 1 0 0 2 1 1 0 0 0 0-2z"/></svg>
        1 555 4817730
      </li>
      <li>
        <svg viewBox="0 0 16 16" aria-hidden="true"><path d="M1 3h14v10H1zm1 1.2V12h12V4.2L8 8.6z"/><path d="M1.5 3.5 8 8l6.5-4.5" fill="none" stroke="#fff" stroke-width="1"/></svg>
        m.penwick@dorventuresinc.example
      </li>
      <li>
        <svg viewBox="0 0 16 16" aria-hidden="true"><circle cx="8" cy="8" r="7.5"/><path d="M1 8h14M8 1c-3 3-3 11 0 14M8 1c3 3 3 11 0 14" fill="none" stroke="#fff" stroke-width="1"/></svg>
        dorventuresinc.example
      </li>
    </ul>

    <div class="brand-mark">
      <div class="brand-circle"></div>
      <div class="brand-name">BRUNVALE</div>
    </div>

    <div class="company-mark">
      <div class="mark-square"></div>
      <div class="mark-name">DOR Ventures Inc.</div>
    </div>
  </section>

</body>
</html>
```